Modern and Improved business card design for Family Dental Practice

We have 2 sets of logo we have designed and now just need a business card layout and design for the office. Colors are on the logo. We can choose which logo we want to go with . The font can be changed to whatever seems modern and relevant. We are family dental office that has been open for over 15 years in South Austin Texas.

Target Market(s)

Handout Business cards to referrals and specialists

Industry/Entity Type

Dental

Contact Information for Business Card

We need address, phone, website and email address. 4830 North Maple Loop Suite 208 , Austin,Texas 78392....phone: 512-847-3195.....email- info@bluepinedental.example....website - BluePineDental.example

Font styles to use
Serif
Decorative

Requirements
Must have
• my logo. We have 2 logos, but we can use just one or if we can incorporate one on one side and the other on the other side.
Nice to have
• Really just need a modern look and clean that incorporates the logo and colors .

```html
<!DOCTYPE html>
<html lang="en">
<head>
<meta charset="utf-8">
<title>Blue Pine Family Dentistry – Business Card</title>
<link rel="stylesheet" href="https://fonts.googleapis.com/css2?family=Montserrat:wght@400;600&family=Questrial&display=swap">
<style>
  :root {
    --backdrop: #e7e2da;
    --card: #ffffff;
    --ink: #1f1f1f;
    --text: #444444;
    --rule: #8a8a8a;
    --green: #2f8a3c;
    --green-head: #4a9a30;
    --green-box: #5aa54a;
  }
  html, body {
    margin: 0;
    padding: 0;
    width: 900px;
    height: 1200px;
    overflow: hidden;
    background: var(--backdrop);
  }
  .canvas {
    position: relative;
    width: 900px;
    height: 1200px;
    font-family: "Montserrat", sans-serif;
    color: var(--text);
  }
  .card {
    position: absolute;
    left: 80px;
    width: 742px;
    height: 440px;
    background: var(--card);
    border-radius: 40px;
    box-shadow: 0 6px 14px rgba(0,0,0,0.25);
  }
  .card--front { top: 132px; }
  .card--back { top: 638px; }

  /* Front */
  .brand-dot {
    position: absolute;
    left: 160px;
    top: 118px;
    width: 130px;
    height: 130px;
    border-radius: 50%;
    background: var(--green);
  }
  .brand-name {
    position: absolute;
    left: 344px;
    top: 120px;
    margin: 0;
    font-family: "Questrial", sans-serif;
    font-weight: 400;
    font-size: 56px;
    line-height: 54px;
    color: var(--ink);
    letter-spacing: 1px;
  }
  .brand-tagline {
    position: absolute;
    left: 346px;
    top: 250px;
    margin: 0;
    font-family: "Questrial", sans-serif;
    font-size: 21px;
    letter-spacing: 2.4px;
    color: var(--green);
  }
  .address {
    position: absolute;
    right: 407px;
    top: 329px;
    margin: 0;
    font-style: normal;
    font-size: 16px;
    line-height: 20px;
    text-align: right;
  }
  .divider {
    position: absolute;
    left: 352px;
    top: 318px;
    width: 2px;
    height: 56px;
    background: var(--green);
  }
  .contacts {
    position: absolute;
    left: 370px;
    top: 311px;
    margin: 0;
    padding: 0;
    list-style: none;
    font-size: 16.5px;
    color: var(--ink);
  }
  .contacts li {
    display: flex;
    align-items: center;
    height: 23px;
  }
  .contacts svg {
    width: 13px;
    height: 13px;
    margin-right: 11px;
    fill: var(--green);
  }

  /* Back */
  .appt-title {
    position: absolute;
    left: 0;
    right: 0;
    top: 74px;
    margin: 0;
    text-align: center;
    font-weight: 600;
    font-size: 30px;
    color: var(--green-head);
  }
  .field-label {
    position: absolute;
    font-size: 16px;
    color: var(--text);
  }
  .field-line {
    position: absolute;
    height: 1px;
    background: var(--rule);
  }
  .days {
    position: absolute;
    left: 35px;
    top: 266px;
    width: 672px;
    display: flex;
    justify-content: space-between;
    font-size: 16px;
  }
  .day {
    display: flex;
    align-items: center;
    gap: 13px;
  }
  .day-box {
    width: 18px;
    height: 18px;
    border: 1.5px solid var(--green-box);
  }
</style>
</head>
<body>
<div class="canvas">

  <section class="card card--front">
    <div class="brand-dot"></div>
    <h1 class="brand-name">BLUE PINE<br>FAMILY</h1>
    <p class="brand-tagline">FAMILY DENTISTRY</p>

    <address class="address">4830 North Maple Loop Suite 208<br>Austin,Texas 78392</address>
    <div class="divider"></div>
    <ul class="contacts">
      <li>
        <svg viewBox="0 0 16 16" aria-hidden="true"><path d="M2 5c0-2 3-3 6-3s6 1 6 3v1h-3V5H5v1H2zM4 7h8l2 6H2z"/></svg>
        512-847-3195
      </li>
      <li>
        <svg viewBox="0 0 16 16" aria-hidden="true"><path d="M1 3h14v10H1zM2 4l6 5 6-5"/><path d="M2 4l6 5 6-5" fill="none" stroke="#fff" stroke-width="1.3"/></svg>
        info@bluepinedental.example
      </li>
      <li>
        <svg viewBox="0 0 16 16" aria-hidden="true"><circle cx="8" cy="8" r="7"/></svg>
        www.BluePineDental.example
      </li>
    </ul>
  </section>

  <section class="card card--back">
    <h2 class="appt-title">Next Appoinment</h2>

    <span class="field-label" style="left:35px;top:148px;">Name</span>
    <div class="field-line" style="left:100px;top:157px;width:605px;"></div>

    <span class="field-label" style="left:35px;top:188px;">Date</span>
    <div class="field-line" style="left:100px;top:202px;width:605px;"></div>

    <div class="days">
      <span class="day">Sun <span class="day-box"></span></span>
      <span class="day">Mon <span class="day-box"></span></span>
      <span class="day">Tue <span class="day-box"></span></span>
      <span class="day">Wed <span class="day-box"></span></span>
      <span class="day">Thu <span class="day-box"></span></span>
      <span class="day">Fri <span class="day-box"></span></span>
      <span class="day">Sat <span class="day-box"></span></span>
    </div>

    <span class="field-label" style="left:37px;top:328px;">Note</span>
    <div class="field-line" style="left:102px;top:337px;width:605px;"></div>
    <div class="field-line" style="left:35px;top:384px;width:672px;"></div>
  </section>

</div>
</body>
</html>
```